Salve Label

2.25 inch round label.

We are looking for a simple label, muted natural colors, sophisticated, elegant, calming.

Name of Product: Herbal Beeswax Salve
This scent is lavender - but there will be others scents
Want this label to be adaptable to other scents with simple color and word changes.

Other things to express on the label - all natural, calming, relaxing

Name of the Company: Tansy Ridge Farm
2 oz.

```html
<!DOCTYPE html>
<html lang="en">
<head>
<meta charset="utf-8">
<title>Herbal Beeswax Salve – Lavender Label</title>
<link rel="stylesheet" href="https://fonts.googleapis.com/css2?family=Montserrat:wght@500;600&family=Oswald:wght@600&display=swap">
<style>
  :root {
    --backdrop: #e4e0dc;
    --scent: #a89cad;
    --scent-deep: #8f8296;
    --paper: #ffffff;
    --comb: #e9e8ec;
    --farm-green: #2f5a3a;
  }
  html, body {
    margin: 0;
    padding: 0;
    width: 1047px;
    height: 1200px;
    overflow: hidden;
    background: var(--backdrop);
  }
  .canvas {
    width: 1047px;
    height: 1200px;
    display: flex;
    align-items: center;
    justify-content: center;
  }
  .label { display: block; }
  .claims-text {
    font-family: "Montserrat", sans-serif;
    font-weight: 500;
    font-size: 38px;
    letter-spacing: 4px;
    fill: var(--paper);
  }
  .farm-name {
    font-family: "Montserrat", sans-serif;
    font-weight: 600;
    font-size: 50px;
    fill: var(--farm-green);
  }
  .product-name {
    font-family: "Oswald", sans-serif;
    font-weight: 600;
    font-size: 64px;
    letter-spacing: 1px;
    fill: var(--paper);
  }
  .scent-name {
    font-family: "Montserrat", sans-serif;
    font-weight: 500;
    font-size: 70px;
    letter-spacing: 2px;
    fill: var(--scent-deep);
  }
  .net-weight {
    font-family: "Montserrat", sans-serif;
    font-weight: 500;
    font-size: 30px;
    fill: var(--paper);
  }
</style>
</head>
<body>
<div class="canvas">
  <svg class="label" width="900" height="900" viewBox="0 0 900 900" xmlns="http://www.w3.org/2000/svg">
    <defs>
      <clipPath id="inner-face">
        <circle cx="450" cy="450" r="370"/>
      </clipPath>
      <path id="claims-arc" d="M 58 450 A 392 392 0 0 1 842 450"/>
    </defs>

    <!-- label base -->
    <circle class="label-base" cx="450" cy="450" r="450" fill="var(--scent)"/>

    <!-- honeycomb field -->
    <g clip-path="url(#inner-face)">
      <rect class="comb-field" x="0" y="560" width="900" height="190" fill="var(--comb)" role="img" aria-label="Soft honeycomb pattern background"/>
    </g>

    <!-- inner white frame -->
    <circle class="inner-frame" cx="450" cy="450" r="372" fill="none" stroke="var(--paper)" stroke-width="5"/>

    <!-- hatched side accents -->
    <path class="hatch-accent" d="M 65 560 A 400 400 0 0 0 148 712" fill="none" stroke="var(--paper)" stroke-width="20" stroke-dasharray="2 5"/>
    <path class="hatch-accent" d="M 752 712 A 400 400 0 0 0 835 560" fill="none" stroke="var(--paper)" stroke-width="20" stroke-dasharray="2 5"/>
    <path class="rule-accent" d="M 148 712 A 400 400 0 0 0 250 796" fill="none" stroke="var(--paper)" stroke-width="3"/>
    <path class="rule-accent" d="M 650 796 A 400 400 0 0 0 752 712" fill="none" stroke="var(--paper)" stroke-width="3"/>

    <!-- claims arc text -->
    <text class="claims-text" text-anchor="middle">
      <textPath href="#claims-arc" startOffset="50%">ALL NATURAL - CALMING - RELAXING</textPath>
    </text>

    <!-- farm name -->
    <circle class="farm-dot" cx="450" cy="250" r="38" fill="var(--farm-green)"/>
    <text class="farm-name" x="450" y="370" text-anchor="middle">Tansy Ridge Farm</text>

    <!-- product name -->
    <text class="product-name" x="450" y="530" text-anchor="middle">HERBAL BEESWAX SALVE</text>

    <!-- scent -->
    <text class="scent-name" x="450" y="680" text-anchor="middle">LAVENDER</text>

    <!-- net weight -->
    <text class="net-weight" x="450" y="795" text-anchor="middle">Net Wt: 2 oz</text>
  </svg>
</div>
</body>
</html>
```